Design a large parking banner – mandatory ticket validation in the shop

Banner Size:
548 cm (width) x 154 cm (height)
Note: The banner will be placed in a metal frame at our parking lot entrance, fully visible to every incoming truck driver. The message must be easy to read from a distance.
Goal of the Banner:
To inform all truck drivers that they must validate their entry ticket inside the shop, even if they are parking for a short time.
The message must be displayed in multiple languages for international drivers.
Mandatory Content:
Main message – in multiple languages (clearly separated or stacked):
Dutch (NL): Vergeet je ticket niet te valideren in de shop – verplicht, ook bij kort parkeren!
French (FR): N'oubliez pas de valider votre ticket à la boutique – obligatoire, même pour un court arrêt !
English (EN): Don't forget to validate your entry ticket in the shop – mandatory, even for short stops!
German (DE): Vergessen Sie nicht, Ihr Einfahrticket im Shop zu entwerten – Pflicht, auch bei kurzem Parken!
Polish (PL): Nie zapomnij zatwierdzić biletu w sklepie – obowiązkowe, nawet przy krótkim postoju!
Romanian (RO): Nu uitați să validați biletul în magazin – obligatoriu, chiar și pentru opriri scurte!
You can include more languages if space allows, but these are essential.
Opening Hours Block (in one section below):
Shop Opening Hours
Mon – Fri: 05:30 – 22:00
Sat & Sun: 08:00 – 22:00
Style & Branding:
The design must match the visual identity of Haulpoint 41Ter
Please refer to the attached photos of existing parking signage for guidance on colors, typography, and layout style
Our logo (attached) must be clearly visible and professionally integrated
Feel free to use icons or pictograms to visually support the message (e.g., ticket, truck, arrow)
Readability is key – large, bold text and high contrast colors that are visible from a distance
Target Audience:
International truck drivers – people who need fast, clear communication. Not everyone speaks the local language, so visual clarity and multilingual messaging are critical.
File Requirements:
Print-ready file (PDF or EPS) – 300 dpi at 1:10 scale
Include 5 cm bleed on all sides
Provide open source files if possible (AI or PSD)

```html
<!DOCTYPE html>
<html lang="en">
<head>
<meta charset="utf-8">
<title>Haulpoint 41Ter – Ticket Validation Banner</title>
<link rel="stylesheet" href="https://fonts.googleapis.com/css2?family=Roboto:ital,wght@0,500;0,700;0,900;1,900&family=Exo+2:wght@700&display=swap">
<style>
  :root {
    --stage: #5c5c5c;
    --paper: #ffffff;
    --ink: #111111;
    --alert-red: #d71920;
    --tag-blue: #1a7fc4;
    --band-blue: #1b82c6;
    --navy: #1d2459;
    --white: #ffffff;
  }
  * { margin: 0; padding: 0; box-sizing: border-box; }
  html, body {
    width: 1200px; height: 505px; overflow: hidden;
    background: var(--stage);
  }
  .banner {
    position: absolute; left: 0; top: 84px;
    width: 1200px; height: 338px;
    background: var(--paper);
    font-family: "Roboto", Arial, sans-serif;
    overflow: hidden;
  }
  .messages { position: absolute; left: 0; top: 0; width: 1200px; height: 212px; }
  .message { position: absolute; }
  .lang-tag {
    display: inline-block;
    background: var(--tag-blue); color: var(--white);
    font-weight: 700; font-size: 14px; line-height: 19px;
    padding: 0 9px 0 10px;
    border-radius: 2px 10px 10px 2px;
    margin-bottom: 7px;
  }
  .line { font-weight: 700; font-size: 16.5px; line-height: 21px; color: var(--ink); white-space: nowrap; }
  .line.tight { line-height: 17px; }
  .line.red { color: var(--alert-red); }
  .col-1 { left: 27px; }
  .col-2 { left: 437px; }
  .col-3 { left: 838px; }
  .row-1 { top: 28px; }
  .row-2 { top: 112px; }

  .hours-band { position: absolute; left: 0; top: 212px; width: 1200px; height: 126px; background: var(--band-blue); overflow: hidden; }
  .hours-band .divider { position: absolute; inset: 0; }
  .hours-title {
    position: absolute; left: 27px; top: 20px;
    font-weight: 900; font-style: italic; font-size: 35px; line-height: 39px;
    color: var(--navy); letter-spacing: -0.3px;
  }
  .slot { position: absolute; top: 21px; width: 254px; text-align: center; }
  .slot-mon { left: 314px; }
  .slot-sat { left: 598px; }
  .day-box {
    position: relative; height: 47px;
    display: flex; align-items: center; justify-content: center; gap: 8px;
  }
  .day-box::before {
    content: ""; position: absolute; inset: 0;
    background: var(--alert-red); transform: skewX(-12deg);
  }
  .day-box svg, .day-box span { position: relative; }
  .day-name { font-weight: 900; font-style: italic; font-size: 35px; color: var(--white); }
  .time {
    font-family: "Exo 2", "Roboto", sans-serif; font-weight: 700; font-size: 29px;
    color: var(--white); margin-top: 2px; letter-spacing: 2px;
  }
  .brand-name {
    position: absolute; left: 880px; width: 320px; top: 44px;
    text-align: center; font-weight: 900; font-size: 30px; color: var(--white);
  }
</style>
</head>
<body>
<div class="banner">
  <div class="messages">
    <div class="message col-1 row-1"><span class="lang-tag">Dutch (NL)</span>
      <p class="line">Vergeet je ticket niet te valideren in de shop</p>
      <p class="line red">verplicht, ook bij kort parkeren!</p></div>
    <div class="message col-2 row-1"><span class="lang-tag">English (EN)</span>
      <p class="line tight">Don't forget to validate your entry ticket<br>in the shop</p>
      <p class="line tight red">mandatory, even for short stops!</p></div>
    <div class="message col-3 row-1"><span class="lang-tag">Polish (PL)</span>
      <p class="line">Nie zapomnij zatwierdzić biletu w sklepie</p>
      <p class="line red">obowiązkowe, nawet przy krótkim postoju!</p></div>
    <div class="message col-1 row-2"><span class="lang-tag">French (FR)</span>
      <p class="line">N'oubliez pas de valider votre ticket à<br>la boutique</p>
      <p class="line red">obligatoire, même pour un court arrêt</p></div>
    <div class="message col-2 row-2"><span class="lang-tag">French (FR)</span>
      <p class="line">Vergessen Sie nicht, Ihr Einfahrticket im<br>Shop zu entwerten</p>
      <p class="line red">Pflicht, auch bei kurzem Parken!</p></div>
    <div class="message col-3 row-2"><span class="lang-tag">Romanian (RO)</span>
      <p class="line">Nu uitați să validați biletul în magazin</p>
      <p class="line red">obligatoriu, chiar și pentru opriri scurte!</p></div>
  </div>

  <div class="hours-band">
    <svg class="divider" width="1200" height="126" viewBox="0 0 1200 126">
      <polygon points="887,0 1200,0 1200,126 858,126" fill="#ffffff"/>
      <polygon points="903,0 1200,0 1200,126 870,126" fill="#1d2459"/>
    </svg>
    <h2 class="hours-title">SHOP OPENING<br>HOURS</h2>

    <div class="slot slot-mon">
      <div class="day-box">
        <svg width="26" height="26" viewBox="0 0 26 26" fill="none" stroke="#1b82c6" stroke-width="2.4">
          <rect x="2" y="4" width="18" height="16" rx="2"/><line x1="2" y1="9" x2="20" y2="9"/>
          <line x1="7" y1="2" x2="7" y2="6"/><line x1="15" y1="2" x2="15" y2="6"/>
          <circle cx="19" cy="19" r="5" fill="#d71920"/><polyline points="19,16.5 19,19 21,20"/>
        </svg>
        <span class="day-name">MON – FRI</span>
      </div>
      <p class="time">05:30 – 22:00</p>
    </div>

    <div class="slot slot-sat">
      <div class="day-box">
        <svg width="26" height="26" viewBox="0 0 26 26" fill="none" stroke="#1b82c6" stroke-width="2.4">
          <rect x="2" y="4" width="18" height="16" rx="2"/><line x1="2" y1="9" x2="20" y2="9"/>
          <line x1="7" y1="2" x2="7" y2="6"/><line x1="15" y1="2" x2="15" y2="6"/>
          <circle cx="19" cy="19" r="5" fill="#d71920"/><polyline points="19,16.5 19,19 21,20"/>
        </svg>
        <span class="day-name">SAT &amp; SUN</span>
      </div>
      <p class="time">08:00 – 22:00</p>
    </div>

    <p class="brand-name">Haulpoint 41Ter</p>
  </div>
</div>
</body>
</html>
```